Brochure design - brisk floors

i need a brochure design for my flooring business which is in the same style/theme as the attached file. the images chosen from clearvault should be focused on quality flooring and presented in a corporate and professional way. this design will be intended for printed brochures which i can hand to my clients as part of the sales process... I have a logo which should be included into the design (attached)
- This design should be ready for "Z" folded leaflet format - similar to the file attached
The design should present the images i attached in the brief
the design should follow the theme of the attached complete, sample brochure
the design needs to present the attached company logo in a clear and impressive way.
the design should allow for text boxes near each of the images

```html
<!DOCTYPE html>
<html lang="en">
<head>
<meta charset="utf-8">
<title>Brisk Floors – Z-fold Brochure</title>
<link href="https://fonts.googleapis.com/css2?family=Nunito+Sans:wght@300;400;600;700&display=swap" rel="stylesheet">
<style>
  :root{
    --teal:#3aa9c4;
    --teal-soft:#5ab3ca;
    --teal-text:#4cb8d3;
    --about-bg:rgba(8,38,48,.93);
    --story-bg:rgba(28,21,14,.9);
    --contact-bg:rgba(232,232,230,.9);
    --wood:#c49a6c;
    --charcoal:#3d3d3d;
    --card:#121212;
    --slate:#4b535b;
    --line:#ffffff;
    --text-light:#f2f2f2;
    --page:#ffffff;
  }
  *{box-sizing:border-box;margin:0;padding:0}
  html,body{width:1200px;height:1200px;overflow:hidden;background:var(--page)}
  body{position:relative;font-family:"Nunito Sans",sans-serif;font-weight:400;color:var(--text-light)}
  .spread{position:absolute;overflow:hidden}
  .spread--outside{left:228px;top:72px;width:751px;height:531px}
  .spread--inside{left:228px;top:627px;width:749px;height:529px;background:var(--charcoal)}
  .layer{position:absolute;left:0;top:0;width:100%;height:100%}
  .box{position:absolute}
  .body-copy{font-size:7.1px;line-height:8.55px;color:var(--text-light);font-weight:400}
  .body-copy p+p{margin-top:8.5px}

  /* outside spread */
  .outside-photo{position:absolute;left:0;top:0;width:100%;height:100%;
    background:
      radial-gradient(ellipse 120px 170px at 570px 200px,rgba(235,225,215,.45),transparent 70%),
      radial-gradient(ellipse 110px 200px at 660px 230px,rgba(60,72,95,.45),transparent 70%),
      linear-gradient(165deg,#d0ab82 0%,#c49a6c 40%,#a98158 75%,#8f6c4b 100%)}
  .about{left:25px;top:103px;width:201px;height:428px;background:var(--about-bg);padding:24px 22px 0 25px}
  .about__title{font-weight:300;font-size:14px;color:var(--teal-text);margin-bottom:6px}
  .story{left:274px;top:0;width:203px;height:356px;background:var(--story-bg);padding:130px 24px 0 26px}
  .contact{left:274px;top:371px;width:203px;height:160px;background:var(--contact-bg);text-align:center}
  .contact__name{position:absolute;left:0;right:0;top:62px;display:flex;justify-content:center;align-items:center;gap:5px;font-weight:400;font-size:12px;letter-spacing:.5px;color:var(--teal)}
  .contact__links{position:absolute;left:0;right:0;top:117px;font-weight:700;font-size:7.5px;line-height:10px;color:var(--teal)}
  .brand{left:545px;top:400px;width:160px;display:flex;flex-direction:column;align-items:center;gap:8px;color:var(--teal);font-weight:400}
  .brand__mark{width:14px;height:14px;background:var(--teal)}
  .brand__name{font-size:17px;letter-spacing:1px}
  .contact .brand__mark{width:8px;height:8px}

  /* inside spread */
  .card{position:absolute;background:var(--card)}
  .card--slate{background:var(--slate)}
  .photo{position:absolute}
  .photo__title{position:absolute;left:8px;bottom:8px;font-weight:400;font-size:13.5px;line-height:17px;color:#fff;text-transform:uppercase;text-shadow:0 0 4px rgba(0,0,0,.35)}
  .card__copy{position:absolute}
  .card__heading{font-weight:400;font-size:13.5px;color:#fff;text-transform:uppercase;margin-bottom:7px}
</style>
</head>
<body>

<!-- Outside spread -->
<section class="spread spread--outside" aria-label="Brochure outside spread">
  <div class="outside-photo" role="img" aria-label="Photograph of a smiling couple lying on a light oak wooden floor, with a teal-tinted room on the left"></div>
  <svg class="layer" viewBox="0 0 751 531" aria-hidden="true">
    <polygon points="0,0 262,0 225,531 0,531" fill="var(--teal-soft)" opacity=".92"/>
    <polygon points="669,0 751,0 751,531 731,531" fill="#5e5e5e" opacity=".9"/>
    <polygon points="477,375 715,240 731,531 477,531" fill="#666" opacity=".88"/>
  </svg>
  <svg class="layer" viewBox="0 0 751 531" aria-hidden="true">
    <polygon points="356,0 374,0 751,190 751,202" fill="var(--line)"/>
    <polygon points="255,531 273,531 751,263 751,249" fill="var(--line)"/>
    <polygon points="667,0 675,0 737,531 729,531" fill="var(--line)"/>
    <polygon points="690,150 751,108 751,116 692,158" fill="var(--line)"/>
  </svg>

  <div class="box about">
    <h2 class="about__title">About us</h2>
    <div class="body-copy">
      <p>Brisk Floors is committed to providing clients, both commercial and private, with the premium flooring service they want, when they want it, and at a price which meets their needs. We are passionate about our service delivery and are renowned as leaders in our field, both technically and aesthetically.</p>
      <p>We concentrate almost exclusively on solid wood restoration and installation. Working with everything from oak parquet and pitch pine to maple leisure floors, with a variety of lacquered and oiled finishes. We have an unrivalled reputation for quality. We are known for supplying a service that works because of the extensive knowledge which we have accumulated through our years of experience.</p>
      <p>The retail and hospitality industries face very specific challenges when it comes to flooring: it must be practical and durable, value for money yet aesthetically pleasing, and it must be fashion forward. Furthermore, our service fits these fast pace industries allowing businesses to remain trading for a long as possible whilst restorations are undertaken.</p>
      <p>Residential Floors have their own specific set of challenges in that most of these flooring projects occur within occupied living space. Our team will always strive to undertake work in a clean and dust-free environment, allowing family spaces to remain safe and liveable.</p>
      <p>Above all, we are an ethical company. Our key values are integrity, decency and fairness; values which underline our relationships with customers, suppliers and staff alike. People are at the heart of our business and we believe that our dedication to improving the job satisfaction and performance of our employees is reflected in the level of service to our clients.</p>
    </div>
  </div>

  <div class="box story body-copy">
    <p>As niam nimaximostia venihitat.<br>Harchictis intiore hentotate venet estem harunt dignis nobit aute li</p>
    <p>bus nonsequis si voluptatia cuptae et aut essum nihic tem. Odita vent.<br>Picia dias voluptam et et labo. Of</p>
    <p>ficid quostio eventis est volore aut aligendam, il idem utatur simporepro optaspi distion sequossitas</p>
    <p>expe consed magnam et volupti onsene velloris sitectore velic to quaspero tenis moloria vel illatio</p>
    <p>nsequia voloreped que dolorecum ad molupta sperio tessinvel essequa spernatur sequis acerene</p>
    <p>quaesto consequam litiistiam, sed quiderundi deniam quamet quodia corporit re, consendaerum</p>
  </div>

  <div class="box contact">
    <div class="contact__name"><span class="brand__mark"></span><span>BRISK FLOORS</span></div>
    <div class="contact__links">www.briskfloors.co.uk<br>info@briskfloors.co.uk</div>
  </div>

  <div class="box brand">
    <span class="brand__mark"></span>
    <span class="brand__name">BRISK FLOORS</span>
  </div>
</section>

<!-- Inside spread -->
<section class="spread spread--inside" aria-label="Brochure inside spread">
  <svg class="layer" viewBox="0 0 749 529" aria-hidden="true">
    <polygon points="487,0 749,0 749,529 532,529" fill="var(--teal)"/>
    <rect x="525" y="0" width="199" height="529" fill="var(--slate)"/>
    <polygon points="0,195 470,0 520,0 0,215" fill="#5a5a5a" opacity=".55"/>
    <polygon points="0,255 749,560 749,575 0,270" fill="#5a5a5a" opacity=".55"/>
    <polygon points="88,0 96,0 26,529 18,529" fill="#5a5a5a" opacity=".55"/>
  </svg>

  <!-- column one -->
  <article class="card" style="left:25px;top:19px;width:199px;height:238px">
    <div class="photo" style="left:9px;top:6px;width:181px;height:164px;background:radial-gradient(ellipse 60px 50px at 120px 80px,rgba(150,160,175,.85),transparent 75%),linear-gradient(150deg,#c9a17e,#a9805f 55%,#7d5d47)" role="img" aria-label="Photo of a floor sanding machine on herringbone parquet">
      <div class="photo__title">Floor sanding<br>&amp; refinishing</div>
    </div>
    <div class="card__copy body-copy" style="left:9px;top:179px;width:184px">Sanding and refinishing hardwood floors is what we do best. Whether your floors have just been installed last week or if they're 100 years old, we'll be able to transform them into exactly what you envision. We will be more than happy to take a look at your floors for you and see what we can do for them to make them look amazing again.</div>
  </article>

  <article class="card" style="left:25px;top:273px;width:199px;height:256px">
    <div class="photo" style="left:9px;top:11px;width:181px;height:161px;background:radial-gradient(ellipse 70px 40px at 130px 60px,rgba(240,235,228,.8),transparent 75%),linear-gradient(175deg,#ece8e2 0%,#c9ac8e 45%,#7a5236 75%,#4a2f1e)" role="img" aria-label="Photo of gloved hands applying wood stain to a floor">
      <div class="photo__title">Floor staining</div>
    </div>
    <div class="card__copy body-copy" style="left:9px;top:181px;width:184px">If you would like to add richness, character and depth to your floor, you may want to consider having them stained. Staining is the process of adding colour to a floor. It's a separate step in the finishing process that is done right after the final sanding and before the finish is applied. This is a highly skilled art form which Brisk Floors have perfected.</div>
  </article>

  <!-- column two -->
  <article class="card" style="left:275px;top:0;width:199px;height:119px">
    <div class="card__copy" style="left:9px;top:22px;width:184px">
      <h3 class="card__heading">Floor repairs</h3>
      <div class="body-copy">Depending on how well your floors have been taken care of – or if there has been renovations done by previous owners – your hardwood floors may have water damaged areas, gaps from relocated walls, pet and pot plant stains, holes, giant gaps, damaged and splintered boards, previous repairs done by an amateur or any other type of damage. Brisk Floors can fix these to perfectly blend with your existing floor.</div>
    </div>
  </article>

  <article class="card" style="left:275px;top:129px;width:199px;height:252px">
    <div class="photo" style="left:9px;top:10px;width:181px;height:173px;background:radial-gradient(ellipse 70px 90px at 50px 100px,rgba(214,160,95,.9),transparent 75%),linear-gradient(150deg,#5e5048,#c98f4f 40%,#b07535 70%,#7e7a78)" role="img" aria-label="Photo of a fitter marking an oak board during floor installation">
      <div class="photo__title">Floor installation</div>
    </div>
    <div class="card__copy body-copy" style="left:9px;top:193px;width:184px">Although hardwood floor sanding &amp; restoration is our main specialty, we also install hardwood floors too. You'll be happy to know that we're fully equipped and skilled to do any wood floor installation our clients need. We have years and years of installation experience and have installed hundreds of floors with great results.</div>
  </article>

  <article class="card" style="left:275px;top:392px;width:199px;height:137px">
    <div class="photo" style="left:9px;top:12px;width:181px;height:99px;background:radial-gradient(ellipse 50px 40px at 130px 40px,rgba(90,90,90,.8),transparent 75%),linear-gradient(180deg,#e0e0e0,#9a9a9a 40%,#4a3a30 75%,#2c211b)" role="img" aria-label="Photo of a worker buffing a dark wooden floor with a polishing machine"></div>
  </article>

  <!-- column three -->
  <article class="card card--slate" style="left:525px;top:0;width:199px;height:257px">
    <div class="photo" style="left:9px;top:25px;width:181px;height:157px;background:radial-gradient(ellipse 60px 40px at 70px 50px,rgba(245,200,150,.7),transparent 75%),linear-gradient(150deg,#e8ab6a,#d08b48 55%,#aa6530)" role="img" aria-label="Photo of hands sanding a wooden stair tread">
      <div class="photo__title">Stair restoration</div>
    </div>
    <div class="card__copy body-copy" style="left:9px;top:192px;width:184px">Nothing will standout more in your space than beautifully restored stairs. A staircase is a high-traffic area and can often become worn with a tired appearance. In order to breathe life into your staircase again a tremendous amount of hand work with specialty tools is needed. At Brisk Floors our team has the skills and expertise to revitalise any staircase and deliver amazing results.</div>
  </article>

  <article class="card card--slate" style="left:525px;top:273px;width:199px;height:256px">
    <div class="photo" style="left:9px;top:11px;width:181px;height:170px;background:radial-gradient(ellipse 60px 50px at 60px 100px,rgba(190,120,80,.7),transparent 75%),linear-gradient(160deg,#35312e,#7e6150 40%,#c49a72 80%,#d2ae88)" role="img" aria-label="Photo of a worker kneeling to lay underlay and subfloor boards">
      <div class="photo__title">Structural<br>floor preparation</div>
    </div>
    <div class="card__copy body-copy" style="left:9px;top:191px;width:184px">For any flooring project the foundations need to be level and structurally sound. Depending on the condition of your subfloor or subframe, it is often necessary to carry out remedial works. Although this can be a lengthy and challenging process, our team will be on-hand to help.</div>
  </article>
</section>

</body>
</html>
```